Tallowmere Consulting Group Business Card Design

We have the logo we just need someone to design a modern business card design.

Name: Leopold Ganzhurt
Phone: 3052918364
Mobile: 9178402297
Web:www.tallowmereconsulting.com
email: lganzhurt@tallowmereconsulting.com
Company: Tallowmere Consulting Group
Title: CEO

Address: 718 Quenby Ave, Miami, Florida 33187

Target Market(s)

companies over 100 employees

Industry/Entity Type

Business

```html
<!DOCTYPE html>
<html lang="en">
<head>
<meta charset="utf-8">
<title>Tallowmere Consulting Group – Business Card</title>
<link rel="stylesheet" href="https://fonts.googleapis.com/css2?family=Arimo:wght@400;700&family=Jost:wght@400&display=swap">
<style>
  :root {
    --canvas: #e9e7e4;
    --card-white: #f7f7f7;
    --brand-blue: #4b73c6;
    --brand-blue-light: #6a8fd6;
    --stripe-grey: #d3d5d9;
    --ink: #555a60;
    --ink-soft: #6d7177;
    --on-blue: #eef2fb;
  }
  * { box-sizing: border-box; margin: 0; padding: 0; }
  html, body { width: 1200px; height: 900px; overflow: hidden; }
  body {
    background: var(--canvas);
    font-family: "Arimo", Arial, sans-serif;
    position: relative;
  }
  .card {
    position: absolute;
    left: 250px;
    width: 700px;
    height: 400px;
    background: var(--card-white);
    overflow: hidden;
    box-shadow: 0 6px 18px rgba(0,0,0,0.18);
  }
  .card--back { top: 35px; }
  .card--front { top: 465px; }

  /* back */
  .back-panel {
    position: absolute; top: 0; left: 0; bottom: 0; width: 300px;
    background: linear-gradient(135deg, var(--brand-blue), var(--brand-blue-light));
  }
  .back-stripe {
    position: absolute; top: 0; bottom: 0; left: 300px; width: 38px;
    background: var(--stripe-grey);
  }
  .brand {
    position: absolute; left: 370px; top: 140px; width: 300px;
    text-align: center; color: var(--ink);
  }
  .brand-mark {
    width: 62px; height: 62px; border-radius: 50%;
    background: var(--brand-blue); margin: 0 auto 14px;
  }
  .brand-name {
    font-weight: 700; font-size: 30px; letter-spacing: 1.5px; line-height: 1;
  }
  .brand-sub {
    font-weight: 700; font-size: 10px; letter-spacing: 2.2px; margin-top: 5px;
  }

  /* front */
  .front-panel {
    position: absolute; top: 0; right: 0; bottom: 0; width: 292px;
    background: linear-gradient(160deg, var(--brand-blue-light), var(--brand-blue));
    color: var(--on-blue);
    font-family: "Jost", Futura, sans-serif;
    padding: 158px 0 0 22px;
  }
  .front-stripe {
    position: absolute; top: 0; bottom: 0; right: 292px; width: 38px;
    background: var(--stripe-grey);
  }
  .person {
    position: absolute; left: 64px; top: 170px; color: var(--ink);
  }
  .person-name { font-weight: 700; font-size: 25px; }
  .person-title { font-size: 15px; color: var(--ink-soft); margin-top: 2px; }
  .address { font-size: 14px; line-height: 1.35; margin-bottom: 18px; }
  .contact-list { list-style: none; font-size: 13.5px; }
  .contact-list li {
    display: flex; align-items: center; gap: 10px; height: 26px; white-space: nowrap;
  }
  .contact-list svg { width: 12px; height: 12px; flex: none; }
</style>
</head>
<body>

<section class="card card--back" aria-label="Card back">
  <div class="back-panel" role="img" aria-label="Blue panel with faint curved line pattern"></div>
  <div class="back-stripe"></div>
  <div class="brand">
    <div class="brand-mark"></div>
    <div class="brand-name">TALLOWMERE</div>
    <div class="brand-sub">CONSULTING GROUP</div>
  </div>
</section>

<section class="card card--front" aria-label="Card front">
  <div class="person">
    <div class="person-name">Leopold Ganzhurt</div>
    <div class="person-title">CEO</div>
  </div>
  <div class="front-stripe"></div>
  <div class="front-panel">
    <p class="address">718 Quenby Ave<br>Miami, Florida 33187</p>
    <ul class="contact-list">
      <li>
        <svg viewBox="0 0 12 12" aria-hidden="true"><path d="M2.5 1 L4.5 1 L5.5 3.5 L4.2 4.5 Q5 7 7.5 7.8 L8.5 6.5 L11 7.5 L11 9.5 Q10.5 11 9 11 Q2 10 1 3 Q1 1.5 2.5 1 Z" fill="currentColor"/></svg>
        (305) 291 8364
      </li>
      <li>
        <svg viewBox="0 0 12 12" aria-hidden="true"><rect x="3" y="0.5" width="6" height="11" rx="1" fill="none" stroke="currentColor" stroke-width="1.2"/><rect x="4.5" y="2" width="3" height="5" fill="currentColor"/></svg>
        (917) 840 2297
      </li>
      <li>
        <svg viewBox="0 0 12 12" aria-hidden="true"><rect x="0.5" y="2.5" width="11" height="7.5" fill="currentColor"/><path d="M0.5 2.5 L6 7 L11.5 2.5" fill="none" stroke="#4b73c6" stroke-width="1"/></svg>
        lganzhurt@tallowmereconsulting.com
      </li>
      <li>
        <svg viewBox="0 0 12 12" aria-hidden="true"><rect x="1" y="1" width="10" height="10" fill="currentColor"/></svg>
        www.tallowmereconsulting.com
      </li>
    </ul>
  </div>
</section>

</body>
</html>
```